Metal Cutting and Forming Company
Vantor Lubricant Works
Metal Cutting and Forming Company - Manufacturing
Creative Brief
Professional
Kent Molloy
Director of Business Development
2715 Elderwick Avenue Detroit, MI 48211-3187
kmolloy@vantorlube.com
vantorlube.com
logo only
plenvik plenvik
Logo images now uploaded

```html
<!DOCTYPE html>
<html lang="en">
<head>
<meta charset="utf-8">
<title>Vantor Lubricant Works – Business Card</title>
<link rel="stylesheet" href="https://fonts.googleapis.com/css2?family=Exo+2:wght@400;600;800&display=swap">
<style>
  :root {
    --page: #e4e6ea;
    --navy-deep: #0c1640;
    --navy: #1c2f7a;
    --navy-light: #3b55b5;
    --paper: #ffffff;
    --paper-shade: #eceef3;
    --ink: #1c2f7a;
    --ink-soft: #55607e;
    --white: #ffffff;
  }
  * { margin: 0; padding: 0; box-sizing: border-box; }
  html, body { width: 1200px; height: 794px; overflow: hidden; }
  body {
    background: var(--page);
    font-family: "Exo 2", Arial, sans-serif;
    display: flex;
    align-items: center;
    justify-content: center;
    gap: 60px;
  }
  .card {
    position: relative;
    width: 520px;
    height: 297px;
    border-radius: 18px;
    overflow: hidden;
    box-shadow: 0 10px 28px rgba(12, 22, 64, 0.25);
  }
  .brand-name {
    font-weight: 800;
    text-transform: uppercase;
    letter-spacing: 1px;
    white-space: nowrap;
    line-height: 1;
  }

  /* Front */
  .card-front {
    background: radial-gradient(circle at 30% 45%, var(--navy-light) 0%, var(--navy) 38%, var(--navy-deep) 100%);
    color: var(--white);
  }
  .front-brand {
    position: absolute;
    left: 0; right: 0; top: 128px;
    text-align: center;
    font-size: 30px;
  }
  .front-web {
    position: absolute;
    right: 28px; bottom: 22px;
    font-size: 11px; letter-spacing: 1px;
    color: rgba(255, 255, 255, 0.75);
  }

  /* Back */
  .card-back {
    background: linear-gradient(135deg, var(--paper) 55%, var(--paper-shade) 100%);
    color: var(--ink);
  }
  .contact-person {
    position: absolute;
    right: 30px; top: 26px;
    text-align: right;
  }
  .person-name { font-size: 20px; font-weight: 600; }
  .person-title { font-size: 11px; color: var(--ink-soft); margin-top: 3px; }
  .back-brand {
    position: absolute;
    left: 30px; top: 118px;
    font-size: 22px;
    color: var(--ink);
  }
  .contact-list {
    position: absolute;
    left: 30px; top: 172px;
    list-style: none;
    font-size: 11px; line-height: 1.6;
    color: var(--ink-soft);
  }
  .contact-list li { display: flex; align-items: center; gap: 7px; }
  .contact-list svg { width: 11px; height: 11px; fill: var(--navy); flex: none; }
  .back-band {
    position: absolute;
    left: 0; right: 0; bottom: 0;
    height: 34px;
    background: linear-gradient(90deg, var(--navy-deep), var(--navy));
    color: var(--white);
    font-size: 11px; letter-spacing: 1px;
    display: flex; align-items: center; padding-left: 30px;
  }
</style>
</head>
<body>

  <section class="card card-front">
    <p class="brand-name front-brand">Vantor Lubricant Works</p>
    <p class="front-web">www.vantorlube.com</p>
  </section>

  <section class="card card-back">
    <div class="contact-person">
      <p class="person-name">Kent Molloy</p>
      <p class="person-title">Director of Business Development</p>
    </div>
    <p class="brand-name back-brand">Vantor Lubricant Works</p>
    <ul class="contact-list">
      <li>
        <svg viewBox="0 0 12 12" aria-hidden="true"><path d="M6 0a4 4 0 0 0-4 4c0 3 4 8 4 8s4-5 4-8a4 4 0 0 0-4-4zm0 5.5A1.5 1.5 0 1 1 6 2.5a1.5 1.5 0 0 1 0 3z"/></svg>
        2715 Elderwick Avenue, Detroit, MI 48211-3187
      </li>
      <li>
        <svg viewBox="0 0 12 12" aria-hidden="true"><path d="M2.5 0.5l2 2.2-1 1.5c.8 1.8 2.3 3.3 4.1 4.1l1.5-1 2.2 2-1 2.2C5 11.5.5 7 .3 1.5z"/></svg>
        (313) 555-0148
      </li>
      <li>
        <svg viewBox="0 0 12 12" aria-hidden="true"><path d="M0 2h12v8H0zM1 3l5 4 5-4v-.2H1z"/></svg>
        kmolloy@vantorlube.com
      </li>
    </ul>
    <div class="back-band">www.vantorlube.com</div>
  </section>

</body>
</html>
```